Flyer für Brötchenlieferdienst
Zielgruppe
Brötchenlieferdienst
Aufgabenstellung
Text und Flyer Format A6, auf dem Flyer sollen ein paar Brötchen abgebildet sein,

```html
<!DOCTYPE html>
<html lang="de">
<head>
<meta charset="utf-8">
<title>Morgenkorb – Flyer Brötchenlieferdienst</title>
<link rel="stylesheet" href="https://fonts.googleapis.com/css2?family=Roboto:wght@400;500;700&display=swap">
<style>
  :root {
    --bg-dark: #1f1f1f;
    --bg-mid: #343434;
    --white: #ffffff;
    --accent: #e6bf3a;
    --badge-yellow: #e8c53c;
    --ink: #1b1b1b;
    --crust: #c88a45;
    --crust-light: #e3b57c;
  }
  * { margin: 0; padding: 0; box-sizing: border-box; }
  html, body { width: 851px; height: 1200px; overflow: hidden; background: var(--bg-dark); }
  body { font-family: "Roboto", Arial, sans-serif; color: var(--white); }

  .flyer {
    position: relative;
    width: 851px;
    height: 1200px;
    overflow: hidden;
    background: radial-gradient(ellipse at 50% 40%, var(--bg-mid) 0%, #262626 55%, var(--bg-dark) 100%);
  }

  .top-band {
    position: absolute;
    left: 0; top: 93px;
    width: 851px; height: 61px;
    background: var(--white);
    border-top: 3px dashed #cfcfcf;
    border-bottom: 3px dashed #cfcfcf;
  }

  .brand-tile {
    position: absolute;
    left: 340px; top: 0;
    width: 157px; height: 236px;
    background: var(--white);
    box-shadow: 0 4px 12px rgba(0,0,0,.35);
    display: flex;
    flex-direction: column;
    align-items: center;
    justify-content: flex-end;
    padding-bottom: 40px;
    gap: 14px;
  }
  .brand-tile .brand-square {
    width: 46px; height: 46px;
    background: var(--ink);
  }
  .brand-tile .brand-name {
    font-size: 27px;
    font-weight: 500;
    color: var(--ink);
    letter-spacing: .5px;
  }

  .headline {
    position: absolute;
    left: 0; top: 268px;
    width: 851px;
    text-align: center;
    font-size: 42px;
    font-weight: 700;
    line-height: 51px;
    white-space: nowrap;
  }
  .headline .highlight { color: var(--accent); }

  .intro {
    position: absolute;
    left: 0; top: 430px;
    width: 851px;
    text-align: center;
    font-size: 25px;
    line-height: 37px;
    white-space: nowrap;
  }
  .intro .highlight { color: var(--accent); }

  .partner {
    position: absolute;
    left: 133px; top: 540px;
    height: 76px;
    display: flex;
    align-items: center;
    gap: 28px;
    font-size: 26px;
  }
  .partner .partner-mark {
    display: flex;
    align-items: center;
    gap: 12px;
    font-weight: 700;
  }
  .partner .partner-square {
    width: 22px; height: 22px;
    background: var(--white);
  }

  .trial-badge {
    position: absolute;
    left: -8px; top: 645px;
    width: 310px; height: 154px;
    background: var(--badge-yellow);
    border: 4px solid var(--white);
    border-radius: 0 22px 22px 0;
    color: var(--ink);
    padding: 14px 0 0 33px;
    white-space: nowrap;
  }
  .trial-badge .trial-lead { font-size: 29px; line-height: 38px; }
  .trial-badge .trial-offer { font-size: 38px; font-weight: 700; line-height: 42px; }

  .trial-text {
    position: absolute;
    left: 336px; top: 658px;
    width: 500px;
    font-size: 24px;
    line-height: 37.5px;
    white-space: nowrap;
  }

  .rolls-photo {
    position: absolute;
    left: 0; top: 810px;
    width: 851px; height: 390px;
    background:
      radial-gradient(ellipse 120px 110px at 570px 100px, var(--crust-light), transparent 100%),
      radial-gradient(ellipse 110px 130px at 220px 170px, var(--crust), transparent 100%),
      radial-gradient(ellipse 110px 90px at 60px 120px, var(--crust), transparent 100%),
      radial-gradient(ellipse 120px 140px at 770px 160px, var(--crust), transparent 100%),
      radial-gradient(ellipse 150px 110px at 460px 250px, #b98a66, transparent 100%),
      radial-gradient(ellipse 170px 90px at 380px 370px, #a55f2a, transparent 100%),
      linear-gradient(180deg, transparent 0%, #222 100%);
  }
</style>
</head>
<body>
<div class="flyer">
  <div class="top-band"></div>

  <div class="brand-tile">
    <div class="brand-square"></div>
    <div class="brand-name">Morgenkorb</div>
  </div>

  <h1 class="headline">Lust auf <span class="highlight">frische Backwaren</span> am Wochen-<br>ende und an den Feiertagen, aber keine<br>Lust zum Bäcker zu gehen?</h1>

  <p class="intro">Dann bestellen Sie Ihre frischen Backwaren bei Morgenkorb und wir<br>liefern Ihnen die Bestellungen <span class="highlight">früh morgens direkt</span> an Ihre Haustür!</p>

  <div class="partner">
    <span>Unsere Partnerbäckerei</span>
    <span class="partner-mark"><span class="partner-square"></span>Backstube Lindner</span>
  </div>

  <div class="trial-badge">
    <div class="trial-lead">Testen Sie unsere</div>
    <div class="trial-offer">kostenlose<br>Probelieferung!</div>
  </div>

  <p class="trial-text">Suchen Sie sich aus unserem Sortiment<br>fünf Brötchen aus, die wir Ihnen gerne am<br>Samstag oder Sonntag liefern.</p>

  <div class="rolls-photo" role="img" aria-label="Foto: verschiedene frische Brötchen und Baguette auf dunklem Untergrund mit Mehl und Körnern"></div>
</div>
</body>
</html>
```